Customer flyer

Hi there,

We need a flyer done for our father's business. It is called Harbor ledger and the flyer will be distributed to realtors in British Columbia. He lends money to realtors when they have sold a home from the time subjects are removed from the transaction to when the sale closes. He is looking for a modern, classy look with the following information:

"Harbor Ledger"

Realtor Pay Day upon Subject Removal

Did you know?

* Fees 100% tax deductable
* Same Day Service
* Confidential
* Low Rates

Your money from 583917 B.C. Ltd. and It can be directly deposited into your bank account or delivered to your office

For quote: call Glen Marsh 236 555 0147

This is a small business so he doesn't have a logo and has never needed to do promotions before as it's run on word of mouth for the past 10 years. We are open to all ideas and suggestions - he is a finance guy so looking to you for the creative side :)

Thank you!

I don't like the phrase Realtor Pay Day upon subject removal. I think I prefer "Realtors! Celebrate Your Home sales upon subject removal" . Your thoughts?

Thank you

```html
<!DOCTYPE html>
<html lang="en">
<head>
<meta charset="utf-8">
<title>Harbor Ledger – Realtor Pay Day</title>
<link href="https://fonts.googleapis.com/css2?family=Alfa+Slab+One&family=Arvo:wght@700&family=Questrial&display=swap" rel="stylesheet">
<style>
  :root {
    --navy: #0d3a6e;
    --navy-deep: #0b2f5c;
    --teal-top: #2a7893;
    --sky-mid: #a9d3df;
    --cream: #f1f2da;
    --sea-light: #bfe3ec;
    --sea-deep: #5fb3cc;
    --gold: #fff200;
    --red: #e0262b;
    --white: #ffffff;
    --subtitle-blue: #1f4fa0;
  }
  html, body {
    margin: 0;
    padding: 0;
    overflow: hidden;
    background: #ffffff;
  }
  .flyer {
    position: relative;
    width: 848px;
    height: 1200px;
    overflow: hidden;
    background: linear-gradient(180deg, var(--teal-top) 0%, #4f97ad 18%, var(--sky-mid) 36%, #e4eee6 52%, var(--cream) 66%, #e8f1e4 78%);
  }
  .hero-photo {
    position: absolute;
    left: 135px;
    top: 14px;
    width: 535px;
    height: 440px;
    background: radial-gradient(ellipse at 50% 65%, #c9a24a 0%, #b28a3a 35%, rgba(160,135,85,0.5) 60%, rgba(90,140,160,0) 78%),
                linear-gradient(180deg, rgba(230,226,207,0.9) 0%, rgba(217,208,176,0.8) 22%, rgba(200,170,100,0) 40%);
    border-radius: 40px;
  }
  .sea-photo {
    position: absolute;
    left: 0;
    top: 905px;
    width: 848px;
    height: 295px;
    background: linear-gradient(180deg, rgba(191,227,236,0.2) 0%, var(--sea-light) 18%, #9fd3e2 45%, var(--sea-deep) 100%);
  }
  .brand-title {
    position: absolute;
    left: 0;
    width: 848px;
    top: 368px;
    margin: 0;
    text-align: center;
    font-family: "Alfa Slab One", serif;
    font-weight: 400;
    font-size: 90px;
    line-height: 1;
    color: var(--navy);
    text-shadow: 3px 0 0 var(--white), -3px 0 0 var(--white), 0 3px 0 var(--white), 0 -3px 0 var(--white),
                 2px 2px 0 var(--white), -2px -2px 0 var(--white), 2px -2px 0 var(--white), -2px 2px 0 var(--white);
  }
  .pay-day {
    position: absolute;
    left: 0;
    width: 904px;
    top: 480px;
    margin: 0;
    text-align: center;
    font-family: "Arvo", serif;
    font-weight: 700;
    font-size: 62px;
    line-height: 1;
    color: var(--gold);
    text-shadow: 2px 0 0 var(--navy), -2px 0 0 var(--navy), 0 2px 0 var(--navy), 0 -2px 0 var(--navy),
                 1px 1px 0 var(--navy), -1px -1px 0 var(--navy), 1px -1px 0 var(--navy), -1px 1px 0 var(--navy);
  }
  .pay-day-note {
    position: absolute;
    left: 0;
    width: 904px;
    top: 549px;
    margin: 0;
    text-align: center;
    font-family: Arial, Helvetica, sans-serif;
    font-weight: 700;
    font-size: 28px;
    letter-spacing: 0.5px;
    color: var(--subtitle-blue);
  }
  .question {
    position: absolute;
    left: 231px;
    top: 600px;
    margin: 0;
    font-family: "Arvo", serif;
    font-weight: 700;
    font-size: 62px;
    letter-spacing: 1px;
    line-height: 1;
    color: var(--navy);
  }
  .deposit-badge {
    position: absolute;
    left: -36px;
    top: 727px;
    width: 399px;
    height: 399px;
    border-radius: 50%;
    background: var(--navy-deep);
  }
  .deposit-text {
    position: absolute;
    left: 43px;
    top: 778px;
    width: 300px;
    margin: 0;
    font-family: "Arvo", serif;
    font-weight: 700;
    font-size: 23px;
    line-height: 37.5px;
    color: var(--white);
  }
  .benefits {
    list-style: none;
    margin: 0;
    padding: 0;
  }
  .benefit {
    position: absolute;
    font-family: "Questrial", sans-serif;
    font-size: 46px;
    letter-spacing: 1px;
    line-height: 1;
    color: var(--navy);
    white-space: nowrap;
  }
  .benefit::before {
    content: "\273D";
    color: var(--red);
    font-size: 34px;
    margin-right: 12px;
    position: relative;
    top: -5px;
  }
  .benefit--tax { left: 172px; top: 686px; }
  .benefit--speed { left: 266px; top: 743px; }
  .benefit--private { left: 336px; top: 800px; }
  .benefit--rates { left: 352px; top: 856px; }
  .contact {
    position: absolute;
    left: 296px;
    width: 520px;
    top: 960px;
    text-align: center;
    color: var(--navy);
  }
  .contact-lead {
    margin: 0;
    font-family: "Questrial", sans-serif;
    font-size: 46px;
    line-height: 56px;
  }
  .contact-name {
    margin: 0;
    font-family: "Arvo", serif;
    font-weight: 700;
    font-size: 64px;
    line-height: 68px;
  }
  .contact-phone {
    margin: 2px 0 0;
    font-family: "Arvo", serif;
    font-weight: 700;
    font-size: 76px;
    line-height: 84px;
    letter-spacing: 1px;
    white-space: nowrap;
  }
</style>
</head>
<body>
  <main class="flyer">
    <div class="hero-photo" role="img" aria-label="Photo of a small house built from stacks of gold coins with a roof of folded banknotes"></div>
    <div class="sea-photo" role="img" aria-label="Photo of calm shallow turquoise sea water"></div>

    <h1 class="brand-title">"Harbor Ledger"</h1>
    <p class="pay-day">Realtor Pay Day</p>
    <p class="pay-day-note">upon Subject Removal</p>

    <h2 class="question">Did you know?</h2>

    <div class="deposit-badge"></div>
    <p class="deposit-text">Your<br>money from<br>583917 B.C. Ltd.<br>and It can be<br>directly deposited<br>into your bank<br>account or<br>delivered to<br>your office</p>

    <ul class="benefits">
      <li class="benefit benefit--tax">Fees 100% tax deductable</li>
      <li class="benefit benefit--speed">Same Day Service</li>
      <li class="benefit benefit--private">Confidential</li>
      <li class="benefit benefit--rates">Low Rates</li>
    </ul>

    <div class="contact">
      <p class="contact-lead">For quote: call</p>
      <p class="contact-name">Glen Marsh</p>
      <p class="contact-phone">236 555 0147</p>
    </div>
  </main>
</body>
</html>
```